Global Weight loss program

we need a business card based in Brooklyn , NY called ZestwellPRO . Mara Tullin Opdegard the founder and creator of ZestwellPRO Movement. A business based around nutrition, health, Whole Foods and fitness.

Industry/Entity Type

Food Service

Contact Information for Business Card

Phone number : 718-402-3859
website www.zestwellpro.example
email : mara@zestwellpro.example

Font styles to use
Sans Serif

Requirements
Must have
• logo colors
• green black and gold
Nice to have
• must be simple and sharp.
Should not have
• pictures of items

```html
<!DOCTYPE html>
<html lang="en">
<head>
<meta charset="utf-8">
<title>ZestwellPRO Business Card</title>
<link rel="stylesheet" href="https://fonts.googleapis.com/css2?family=Work+Sans:wght@400;500;600&display=swap">
<style>
  :root {
    --stage: #e6e6e4;
    --card-white: #ffffff;
    --card-black: #1c1c1c;
    --pattern-tone: #2a2a2a;
    --ink: #2b2b2b;
    --ink-soft: #555555;
    --green: #7cc142;
    --gold: #c9a23a;
    --white: #ffffff;
  }
  * { box-sizing: border-box; margin: 0; padding: 0; }
  html, body {
    width: 1200px; height: 900px; overflow: hidden;
    background: var(--stage);
    font-family: "Work Sans", Arial, sans-serif;
  }
  .canvas { position: relative; width: 1200px; height: 900px; }
  .card {
    position: absolute; left: 250px;
    width: 700px; height: 400px;
    border-radius: 26px; overflow: hidden;
    box-shadow: 0 10px 28px rgba(0,0,0,.18);
  }
  .card--back { top: 40px; background: var(--card-black); }
  .card--front { top: 470px; background: var(--card-white); }

  .back-pattern { position: absolute; inset: 0; width: 100%; height: 100%; }
  .back-brand {
    position: absolute; inset: 0;
    display: flex; flex-direction: column; align-items: center; justify-content: center;
  }
  .brand-mark { width: 70px; height: 70px; background: var(--gold); margin-bottom: 18px; }
  .wordmark { font-weight: 600; font-size: 54px; letter-spacing: -1px; line-height: 1; }
  .card--back .wordmark { color: var(--white); }
  .card--front .wordmark { color: var(--ink); font-size: 40px; }
  .tagline { margin-top: 10px; font-size: 14px; letter-spacing: 3px; }
  .card--back .tagline { color: var(--white); }
  .card--front .tagline { color: var(--ink-soft); font-size: 11px; letter-spacing: 2.2px; }

  .front-brand {
    position: absolute; left: 40px; top: 0; width: 280px; height: 100%;
    display: flex; flex-direction: column; align-items: center; justify-content: center;
  }
  .front-brand .brand-mark { width: 56px; height: 56px; margin-bottom: 16px; }
  .divider {
    position: absolute; left: 340px; top: 90px; width: 2px; height: 220px; background: var(--ink);
  }
  .contact { position: absolute; left: 380px; top: 92px; color: var(--ink); }
  .contact__name {
    color: var(--green); font-weight: 500; font-size: 27px; letter-spacing: 2px; line-height: 1;
  }
  .contact__role { font-size: 18px; margin-top: 6px; color: var(--ink-soft); }
  .contact__address { font-size: 18px; line-height: 1.35; margin-top: 14px; }
  .contact__lines { list-style: none; margin-top: 10px; font-size: 18px; line-height: 1.45; }
  .contact__lines li { display: flex; align-items: center; gap: 12px; }
  .contact__lines svg { width: 14px; height: 14px; flex: none; }
</style>
</head>
<body>
<main class="canvas">
  <section class="card card--back">
    <svg class="back-pattern" role="img" aria-label="Faint repeating pattern of small figure silhouettes across the dark card" viewBox="0 0 700 400" preserveAspectRatio="none">
      <rect width="700" height="400" fill="var(--card-black)"/>
      <rect width="700" height="400" fill="var(--pattern-tone)" opacity=".5"/>
    </svg>
    <div class="back-brand">
      <div class="brand-mark"></div>
      <div class="wordmark">ZestwellPRO</div>
      <div class="tagline">Fitness, Nutrition and Health</div>
    </div>
  </section>

  <section class="card card--front">
    <div class="front-brand">
      <div class="brand-mark"></div>
      <div class="wordmark">ZestwellPRO</div>
      <div class="tagline">Fitness, Nutrition and Health</div>
    </div>
    <div class="divider"></div>
    <div class="contact">
      <h1 class="contact__name">MARA OPDEGARD</h1>
      <p class="contact__role">Founder</p>
      <p class="contact__address">88 Marlow St.<br>Brooklyn, NY 11201</p>
      <ul class="contact__lines">
        <li>
          <svg viewBox="0 0 14 14" aria-hidden="true"><path d="M3 1.5l2.2 0 .8 3-1.4 1a7 7 0 0 0 3.9 3.9l1-1.4 3 .8v2.2c0 .6-.5 1.1-1.1 1.1A10.5 10.5 0 0 1 1.9 2.6c0-.6.5-1.1 1.1-1.1z" fill="var(--green)"/></svg>
          718-402-3859
        </li>
        <li>
          <svg viewBox="0 0 14 14" aria-hidden="true"><rect x="1" y="3" width="12" height="8.5" rx="1" fill="none" stroke="var(--green)" stroke-width="1.4"/><path d="M1.5 3.5L7 8l5.5-4.5" fill="none" stroke="var(--green)" stroke-width="1.4"/></svg>
          mara@zestwellpro.example
        </li>
        <li>
          <svg viewBox="0 0 14 14" aria-hidden="true"><circle cx="7" cy="7" r="5.8" fill="none" stroke="var(--green)" stroke-width="1.3"/><ellipse cx="7" cy="7" rx="2.5" ry="5.8" fill="none" stroke="var(--green)" stroke-width="1.1"/><path d="M1.2 7h11.6" stroke="var(--green)" stroke-width="1.1"/></svg>
          www.zestwellpro.example
        </li>
      </ul>
    </div>
  </section>
</main>
</body>
</html>
```